Stationary design for real estate company in Trinidad and Tobago

Kestra Realty Ltd. , real estate company operating in Trinidad and Tobago, requires a sleek, modern and professional stationary package to wow our customers and potential new clients. we want to look sleek and professional; first impressions count in this business!
Business Address:
Level 1, Marlowe Point Tower
4C Seldon Grove Boulevard
Marlowe Point
Colwyn Pereira Highway
Port of Spain
Trinidad
Tel: + 1 868 555 0147
www.kestra-tt.com
info@kestra-tt.com

```html
<!DOCTYPE html>
<html lang="en">
<head>
<meta charset="utf-8">
<title>Kestra Realty – Business Card</title>
<link rel="stylesheet" href="https://fonts.googleapis.com/css2?family=Montserrat:wght@500;700&family=Roboto:wght@400&display=swap">
<style>
  :root {
    --backdrop: #999999;
    --paper: #f7f7f5;
    --navy: #1e3a6b;
    --navy-deep: #132a5c;
    --gold: #c9a45a;
    --ink-grey: #6f6f6f;
    --white: #ffffff;
  }
  * { margin: 0; padding: 0; box-sizing: border-box; }
  html, body { width: 1200px; height: 1021px; overflow: hidden; }
  body {
    background: var(--backdrop);
    position: relative;
    font-family: "Roboto", Arial, sans-serif;
  }
  .card {
    position: absolute;
    left: 270px;
    width: 660px;
    height: 377px;
    border-radius: 3px;
    box-shadow: 0 10px 28px rgba(0,0,0,0.25);
  }
  .card--front { top: 110px; background: var(--paper); }
  .card--back  { top: 533px; background: var(--navy-deep); }

  .brand {
    position: absolute;
    display: flex;
    align-items: center;
    gap: 14px;
    font-family: "Montserrat", Arial, sans-serif;
    font-weight: 500;
    letter-spacing: 0.08em;
    white-space: nowrap;
  }
  .brand__dot { border-radius: 50%; background: var(--gold); flex: none; }
  .card--front .brand { left: 56px; top: 48px; font-size: 30px; color: var(--navy); }
  .card--front .brand__dot { width: 34px; height: 34px; }
  .card--back .brand {
    left: 50%; top: 50%; transform: translate(-50%, -50%);
    font-size: 52px; color: var(--white);
  }
  .card--back .brand__dot { width: 56px; height: 56px; }

  .address {
    position: absolute;
    left: 56px; top: 122px;
    font-size: 15.5px;
    line-height: 1.32;
    color: var(--ink-grey);
  }
  .contacts {
    position: absolute;
    left: 56px; top: 238px;
    list-style: none;
    font-size: 15.5px;
    line-height: 1.5;
    color: var(--ink-grey);
  }
  .contacts li { display: flex; align-items: center; gap: 10px; }
  .contacts svg { width: 15px; height: 15px; flex: none; }

  .holder {
    position: absolute;
    right: 56px; bottom: 46px;
    text-align: left;
  }
  .holder__name {
    font-family: "Montserrat", Arial, sans-serif;
    font-weight: 700;
    font-size: 19px;
    letter-spacing: 0.02em;
    color: var(--navy);
  }
  .holder__title {
    font-size: 16px;
    color: var(--gold);
    margin-top: 2px;
  }
</style>
</head>
<body>

<section class="card card--front">
  <div class="brand"><span class="brand__dot"></span>KESTRA REALTY</div>

  <address class="address" style="font-style:normal">
    Level 1, Marlowe Point Tower<br>
    4C Seldon Grove Boulevard<br>
    Marlowe Point Colwyn Pereira Highway<br>
    Port of Spain Trinidad
  </address>

  <ul class="contacts">
    <li>
      <svg viewBox="0 0 16 16" aria-hidden="true"><path fill="#c9a45a" d="M3.6 1.2l2.2 2.6c.3.4.3.9 0 1.2L4.7 6.2c.8 1.9 2.3 3.4 4.2 4.3l1.2-1.2c.3-.3.9-.4 1.2 0l2.6 2.2c.4.3.4.9.1 1.3l-1.2 1.4c-.4.5-1.1.7-1.7.5C6.2 13.2 2.8 9.8 1.3 4.9c-.2-.6 0-1.3.5-1.7L3 1.1c.2-.2.5-.1.6.1z"/></svg>
      + 1 868 555 0147
    </li>
    <li>
      <svg viewBox="0 0 16 16" aria-hidden="true"><rect x="1" y="3" width="14" height="10" fill="none" stroke="#c9a45a" stroke-width="1.3"/><path d="M1 3.5l7 5.5 7-5.5" fill="none" stroke="#c9a45a" stroke-width="1.3"/></svg>
      info@kestra-tt.com
    </li>
    <li>
      <svg viewBox="0 0 16 16" aria-hidden="true"><g fill="none" stroke="#c9a45a" stroke-width="1.1"><circle cx="8" cy="8" r="6.5"/><ellipse cx="8" cy="8" rx="3" ry="6.5"/><path d="M1.5 8h13M2.5 4.8h11M2.5 11.2h11"/></g></svg>
      www.kestra-tt.com
    </li>
  </ul>

  <div class="holder">
    <p class="holder__name">DAVIN R. HALLOWAY</p>
    <p class="holder__title">Founder &amp; CEO</p>
  </div>
</section>

<section class="card card--back">
  <div class="brand"><span class="brand__dot"></span>KESTRA REALTY</div>
</section>

</body>
</html>
```